Business Card for Multi-Brand Sportswear Company

We are looking for a business card which represents our company and the multiple brands within it.

The company: Kelt Athletic (LTD)
The brands: Kelt, PawaLuni, VerdantFlex, Grit and Gale

Employees using these cards would be representing Kelt Athletic, rather than any of the individual brands. You will see a current design within the uploaded files, to give some inspiration. The actual text of the brands is not necessary, but the logos should be on there is some format.

Our creative minds on this are stretched, so we are looking for someone to make this their own, and show us what a good business card should look like.

We may like to get these printed with spot gloss, so keep that in mind with your designs.

www.keltathletic.co.uk

Industry/Entity Type

Business

Contact Information for Business Card

Tom Hollingsworth-Pryce
Operations Manager
(+44) 1632 960 418
Tom@keltathletic.co.uk
www.keltathletic.co.uk

Font styles to use
Sans Serif
Other font styles liked:
• Eurostile

Colors
ffffff

Requirements
Nice to have
• Dark (black) background

```html
<!DOCTYPE html>
<html lang="en">
<head>
<meta charset="utf-8">
<title>Kelt Athletic – Business Card</title>
<link href="https://fonts.googleapis.com/css2?family=Archivo:wght@400;600;800&family=Michroma&display=swap" rel="stylesheet">
<style>
  :root {
    --page: #e6e4e2;
    --card: #1f232b;
    --band: #2b3037;
    --band-light: #33383f;
    --faint: #262a32;
    --faint-line: #2e333b;
    --faint-text: #3a3f48;
    --white: #ffffff;
    --muted: #d9dbde;
    --rule: #7b8088;
    --accent: #e0202f;
  }
  * { box-sizing: border-box; margin: 0; padding: 0; }
  html, body { width: 1200px; height: 1200px; overflow: hidden; }
  body { background: var(--page); position: relative; font-family: "Archivo", Arial, sans-serif; }

  .card {
    position: absolute;
    top: 466px;
    width: 422px;
    height: 236px;
    background: var(--card);
    overflow: hidden;
    box-shadow: 0 6px 18px rgba(0,0,0,.25);
  }
  .card--front { left: 122px; }
  .card--back { left: 640px; }

  /* front: faint sub-brand tiles */
  .brand-tile {
    position: absolute;
    background: var(--faint);
    border: 1px solid var(--faint-line);
    color: var(--faint-text);
    font-family: "Archivo", Arial, sans-serif;
    font-size: 8px;
    font-weight: 600;
    white-space: nowrap;
    display: flex; align-items: center; justify-content: center;
    letter-spacing: .03em;
  }
  .tile-a { left: 4px;  top: 34px; width: 62px; height: 40px; }
  .tile-b { left: 145px; top: 40px; width: 66px; height: 36px; }
  .tile-c { left: 84px; top: 58px; width: 40px; height: 40px; border-radius: 50%; }
  .tile-d { left: 14px; top: 98px; width: 30px; height: 30px; border-radius: 50%; }
  .tile-e { left: 14px; top: 145px; width: 44px; height: 36px; }

  .front-mark {
    position: absolute;
    left: 150px; top: 100px;
    display: flex; align-items: center; gap: 8px;
  }
  .front-mark .dot { width: 10px; height: 10px; background: var(--accent); }
  .front-mark .name {
    font-family: "Michroma", Arial, sans-serif;
    font-size: 30px; color: var(--white); letter-spacing: .04em;
  }

  /* back */
  .header-band {
    position: absolute; left: 0; top: 32px; width: 340px; height: 39px;
    background: var(--band);
  }
  .header-band .band-fill {
    position: absolute; left: 0; top: 0; width: 130px; height: 39px;
    background: linear-gradient(90deg, var(--band-light), var(--band));
  }
  .back-mark {
    position: absolute; left: 140px; top: 37px;
    display: flex; align-items: center; gap: 8px;
  }
  .back-mark .dot { width: 7px; height: 7px; background: var(--accent); }
  .back-mark .name {
    font-family: "Michroma", Arial, sans-serif;
    font-size: 18px; color: var(--white); letter-spacing: .04em;
  }
  .back-mark .word { display: flex; flex-direction: column; margin-left: 4px; }
  .back-mark .word strong {
    font-family: "Michroma", Arial, sans-serif; font-weight: 400;
    font-size: 11px; color: var(--white); letter-spacing: .06em; line-height: 1.1;
  }
  .back-mark .word small {
    font-size: 4.5px; color: var(--muted); letter-spacing: .05em;
  }

  .person { position: absolute; left: 19px; top: 128px; }
  .person .full-name { font-weight: 800; font-size: 12.5px; color: var(--white); letter-spacing: .08em; white-space: nowrap; }
  .person .role { font-size: 10.5px; color: var(--muted); letter-spacing: .08em; margin-top: 3px; }

  .divider { position: absolute; left: 209px; top: 133px; width: 2px; height: 28px; background: var(--rule); }

  .contacts { position: absolute; left: 228px; top: 117px; list-style: none; }
  .contacts li {
    display: flex; align-items: center; gap: 14px;
    height: 22px; font-weight: 600; font-size: 11.5px; color: var(--white); letter-spacing: .1em;
    white-space: nowrap;
  }
  .contacts svg { flex: none; }
</style>
</head>
<body>

<section class="card card--front" aria-label="Business card front">
  <div class="brand-tile tile-a">PawaLuni</div>
  <div class="brand-tile tile-b">VerdantFlex</div>
  <div class="brand-tile tile-c"></div>
  <div class="brand-tile tile-d"></div>
  <div class="brand-tile tile-e"></div>
  <div class="front-mark">
    <span class="name">Kelt</span>
    <span class="dot"></span>
  </div>
</section>

<section class="card card--back" aria-label="Business card back">
  <div class="header-band">
    <div class="band-fill" role="img" aria-label="Dynamic graphic accent area"></div>
  </div>
  <div class="back-mark">
    <span class="name">Kelt</span>
    <span class="dot"></span>
    <span class="word"><strong>ATHLETIC</strong><small>PERFORMANCE WEAR</small></span>
  </div>

  <div class="person">
    <p class="full-name">Tom Hollingsworth-Pryce</p>
    <p class="role">Operations Manager</p>
  </div>
  <div class="divider"></div>

  <ul class="contacts">
    <li><svg width="9" height="9" viewBox="0 0 9 9"><path d="M1 1L8 8M8 1L1 8" stroke="#fff" stroke-width="2"/></svg>(+44) 1632 960 418</li>
    <li><svg width="9" height="9" viewBox="0 0 9 9"><path d="M1 1L8 8M8 1L1 8" stroke="#fff" stroke-width="2"/></svg>Tom@keltathletic.co.uk</li>
    <li><svg width="9" height="9" viewBox="0 0 9 9"><path d="M1 1L8 8M8 1L1 8" stroke="#fff" stroke-width="2"/></svg>www.keltathletic.co.uk</li>
  </ul>
</section>

</body>
</html>
```